Halloween Style Website Design

We need a website design with a Halloween theme.

I have provided 3 wireframes to work from. If you like you can just design the homepage first. If we like your designs we will instruct you to design the other pages once we narrow them down.

The website will be totally halloween themed. We will use vector type designs.

We want a feel similar to this style I guess:

https://v.clipvarn.net/pic/Kt7mQ2wLx9aR/largestill.jpg
https://media.sketchlorn.com/members/5172804/captures/3318467/panel_2__2_.jpg
https://img4.plotmerrow.com/p/1000x1000/41/09/halloween-castle-background-design-vector-58301746.jpg
https://pix.graventa.com/free-vector/decorative-halloween-background-flat-style_48-7715302946.jpg?size=626&ext=jpg
https://bx7.quillomedia.net/jpg/05/31/96/48/500_K_531964827_rTmWbZeLoNcYpQ4sVhGaJdKiUvXyFe2s.jpg

```html
<!DOCTYPE html>
<html lang="en">
<head>
<meta charset="utf-8">
<title>Pumpkin Lane — Home</title>
<link href="https://fonts.googleapis.com/css2?family=Mystery+Quest&family=Poppins:wght@400;500;600&family=Roboto:wght@400;500;700&display=swap" rel="stylesheet">
<style>
:root{
  --orange:#f0841c;
  --teal:#1fb5a5;
  --ink:#111;
  --muted:#7a7a7a;
  --grey-btn:#b8b8b8;
  --white:#fff;
}
*{box-sizing:border-box;margin:0;padding:0}
html,body{width:681px;height:1200px;overflow:hidden;background:var(--white)}
.page{position:relative;width:681px;height:1200px;font-family:"Roboto",sans-serif;color:var(--ink)}
.abs{position:absolute}

.brand{left:66px;top:50px;font-family:"Poppins",sans-serif;font-weight:600;font-size:17px;color:var(--orange);letter-spacing:.3px}
.nav{left:305px;top:59px;display:flex;gap:10px;font-family:"Poppins",sans-serif;font-weight:500;font-size:8.5px}
.login{left:512px;top:58px;font-family:"Poppins",sans-serif;font-size:9px;color:#bdbdbd}
.signup{left:551px;top:54px;width:57px;height:21px;background:var(--orange);color:var(--white);font-family:"Poppins",sans-serif;font-weight:500;font-size:7px;display:flex;align-items:center;justify-content:center}

.hero-art{left:56px;top:101px;width:245px;height:173px;background:radial-gradient(circle at 45% 30%,#bfe4d6 0,#6bb8ad 18%,#0f8c95 40%,#064a57 75%,#03242b 100%)}
.hero-title{left:329px;top:118px;width:270px;font-family:"Mystery Quest",serif;font-weight:400;font-size:31px;line-height:33px;color:var(--orange);letter-spacing:.5px}
.hero-text{left:329px;top:193px;width:250px;font-family:"Poppins",sans-serif;font-size:7px;line-height:12.5px;color:var(--muted)}
.learn{left:330px;top:229px;width:73px;height:19px;border:1.5px solid #3b8fd6;font-family:"Roboto",sans-serif;font-weight:500;font-size:9.5px;display:flex;align-items:center;justify-content:center}

.card{top:312px;height:184px;border-radius:2px;overflow:hidden;color:var(--white)}
.card-build{left:55px;width:187px;background:linear-gradient(180deg,#9a3d0a 0%,#b4520f 45%,#3b1d10 80%,#1a1411 100%)}
.card-tricks{left:248px;width:187px;background:radial-gradient(circle at 50% 25%,#3c5a52 0,#193431 45%,#0e2020 100%)}
.card-treets{left:441px;width:180px;background:radial-gradient(circle at 80% 85%,#6a4425 0,#2a1d16 40%,#121015 100%)}
.card h2{position:absolute;top:14px;left:0;right:0;text-align:center;font-family:"Mystery Quest",serif;font-weight:400;font-size:30px;color:var(--orange)}
.card p{position:absolute;left:22px;right:12px;top:56px;font-size:7px;line-height:12.5px}
.card b{font-weight:700}
.read{position:absolute;left:50%;transform:translateX(-50%);top:152px;width:67px;height:20px;background:var(--teal);border-radius:3px;font-size:7px;font-weight:500;display:flex;align-items:center;justify-content:center}

.totop{left:653px;width:20px;height:20px;background:var(--grey-btn);display:flex;align-items:center;justify-content:center}

.pumpkin-art{left:56px;top:522px;width:190px;height:115px;background:radial-gradient(circle at 50% 40%,#d9701b 0,#8a3a0c 30%,#1b0d06 70%,#050302 100%)}
.about{left:265px;top:522px;width:220px;font-family:"Poppins",sans-serif;font-size:8.3px;line-height:15px;color:var(--muted)}
.about b{font-weight:600}
.signup-now{left:520px;top:568px;font-family:"Poppins",sans-serif;font-weight:500;font-size:13.5px;color:var(--teal)}

.banner{left:56px;top:668px;width:570px;height:169px;background:linear-gradient(90deg,#5b4a3a 0%,#4d3a2a 35%,#8a3b10 60%,#a94712 85%,#8a3a12 100%)}
.banner h2{position:absolute;left:25px;top:18px;font-family:"Mystery Quest",serif;font-weight:400;font-size:24px;letter-spacing:1.5px;color:var(--white)}
.banner p{position:absolute;left:25px;top:56px;width:525px;font-size:7px;line-height:12.5px;color:var(--white)}
.connect{position:absolute;left:25px;top:124px;width:86px;height:20px;background:var(--teal);border-radius:3px;color:var(--white);font-size:7px;font-weight:500;display:flex;align-items:center;justify-content:center}

.rule{left:134px;top:854px;width:414px;height:1.5px;background:var(--ink)}
.foot-nav{left:0;width:681px;top:868px;display:flex;justify-content:center;gap:10px;font-family:"Poppins",sans-serif;font-weight:500;font-size:12px}
.copy{left:0;width:681px;top:887px;text-align:center;font-family:"Roboto",sans-serif;font-size:9.5px}
.copy u{text-underline-offset:2px}
</style>
</head>
<body>
<div class="page">
  <header>
    <div class="abs brand">Pumpkin Lane</div>
    <nav class="abs nav"><span>Home</span><span>Build</span><span>Tricks</span><span>Treets</span></nav>
    <div class="abs login">Login</div>
    <div class="abs signup">Sign Up</div>
  </header>

  <section>
    <div class="abs hero-art" role="img" aria-label="Illustration of a haunted castle under a full moon with bats and bare trees"></div>
    <h1 class="abs hero-title">WELCOME TO<br>PUMPKIN LANE!</h1>
    <p class="abs hero-text">Lorem ipsum dolor sit amet, consectetur adipiscing elit. Ut elit tellus, luctus nec ullamcorper mattis, pulvinar dapibus leo.</p>
    <div class="abs learn">LEARN MORE</div>
  </section>

  <section>
    <article class="abs card card-build" role="img" aria-label="Orange graveyard scene with bats and a cobweb">
      <h2>BUILD</h2>
      <p><b>Lorem Ipsum</b> is simply dummy text of the printing and typesetting industry. Lorem Ipsum has been the industry’s standard dummy text ever since the 1500s, when an unknown printer took a galley of type and scrambled it to make a type specimen book. It has survived not only five centuries,</p>
      <div class="read">Read More</div>
    </article>
    <article class="abs card card-tricks" role="img" aria-label="Dark teal night scene with a moon and a graveyard">
      <h2>TRICKS</h2>
      <p><b>Lorem Ipsum</b> is simply dummy text of the printing and typesetting industry. Lorem Ipsum has been the industry’s standard dummy text ever since the 1500s, when an unknown printer took a galley of type and scrambled it to make a type specimen book. It has survived not only five centuries,</p>
      <div class="read">Read More</div>
    </article>
    <article class="abs card card-treets" role="img" aria-label="Dark scene with candles and an open spell book">
      <h2>TREETS</h2>
      <p><b>Lorem Ipsum</b> is simply dummy text of the printing and typesetting industry. Lorem Ipsum has been the industry’s standard dummy text ever since the 1500s, when an unknown printer took a galley of type and scrambled it to make a type specimen book. It has survived not only five centuries,</p>
      <div class="read">Read More</div>
    </article>
  </section>

  <section>
    <div class="abs pumpkin-art" role="img" aria-label="Carved pumpkins on a dark background with a Halloween October 31 title"></div>
    <p class="abs about"><b>Lorem Ipsum</b> is simply dummy text of the printing and typesetting industry. Lorem Ipsum has been the industry’s standard dummy text ever since the 1500s, when an unknown printer took a galley of type and scrambled it to make a type specimen book. It has survived not only five centuries, but also the leap into electronic typesetting, remaining essentially unchanged.</p>
    <div class="abs signup-now">Sign Up Now</div>
  </section>

  <section>
    <div class="abs banner" role="img" aria-label="Graveyard at dusk with a castle, a large moon and twisted trees">
      <h2>HAPPY HALLOWEEN</h2>
      <p>Lorem ipsum dolor sit amet, consectetur adipiscing elit. Ut elit tellus, luctus nec ullamcorper mattis, pulvinar dapibus leo.It is a long established fact that a reader will be distracted by the readable content of a page when looking at its layout. The point of using Lorem Ipsum is that it has a more-or-less normal distribution of letters, as opposed to using ‘Content here, content here’, making it look like readable English. Many desktop publishing packages and web page editors now use Lorem Ipsum as their default model text, and a search for ‘lorem ipsum’ will uncover many web sites still in their infancy.</p>
      <div class="connect">LET’S CONNECT</div>
    </div>
  </section>

  <footer>
    <div class="abs rule"></div>
    <nav class="abs foot-nav"><span>Home</span><span>build</span><span>Tricks</span><span>Treets</span></nav>
    <p class="abs copy">Copyright @ 2020 - pumpkin lane - <u>privacy poolicy</u></p>
  </footer>

  <div class="abs totop" style="top:298px"><svg width="8" height="6" viewBox="0 0 8 6"><path d="M1 5 4 2 7 5" fill="none" stroke="#fff" stroke-width="1.6"/></svg></div>
  <div class="abs totop" style="top:488px"><svg width="8" height="6" viewBox="0 0 8 6"><path d="M1 5 4 2 7 5" fill="none" stroke="#fff" stroke-width="1.6"/></svg></div>
  <div class="abs totop" style="top:717px"><svg width="8" height="6" viewBox="0 0 8 6"><path d="M1 5 4 2 7 5" fill="none" stroke="#fff" stroke-width="1.6"/></svg></div>
  <div class="abs totop" style="top:945px"><svg width="8" height="6" viewBox="0 0 8 6"><path d="M1 5 4 2 7 5" fill="none" stroke="#fff" stroke-width="1.6"/></svg></div>
  <div class="abs totop" style="top:1174px"><svg width="8" height="6" viewBox="0 0 8 6"><path d="M1 5 4 2 7 5" fill="none" stroke="#fff" stroke-width="1.6"/></svg></div>
</div>
</body>
</html>
```